Design for Cedar Lark Homes real estate agency

Incorporate logo into new business cards. I need to include the Brindley Vance logo incorporated into Cedar Lark Homes on one side of the card (attached). On the other side I see just the icon with "Maren Quill" (attached) with "Connected by Trust" either included as is or removed from logo and rather put as a tag line on the business card separate from the main logo. Contact information:

Maren Quill
Associate Broker
Cell: 730-418-5093
Email: marenquill@cedarlarkhomes.example
Web: www.cedarlarkhomes.example

Target Market(s)

Buyers, Sellers, Builders and Investors of homes and land

Industry/Entity Type

Real Estate Agent

Contact Information for Business Card

My client base tend to be higher end home buyers, sellers, builders and investors. I have been more and more in land and subdivisions for builders and investors. The card should not be cluttered. Clean and simple - yet with an air of exclusive/high end

Colors

Designer to choose colors to be used in the design.

Requirements
Must have
• Must have the logo on one side that has Brindley Vance logo incorporated. The side that has my contact information does not have to have the Brindley Vance logo incorporated.
• Must include "Connected by Trust" tag line either within logo (as is) or removed from logo and included in another position on the side of the business card with contact information.
Should not have
• Should not have Brindley Vance logo incorporated into Cedar Lark Homes logo on both sides of business card. Would like the Cedar Lark Homes logo that has Brindley Logo only on the back side of card without contact information.

```html
<!DOCTYPE html>
<html lang="en">
<head>
<meta charset="utf-8">
<title>Cedar Lark Homes – Business Cards</title>
<link rel="stylesheet" href="https://fonts.googleapis.com/css2?family=Cinzel:wght@400;600&family=Montserrat:wght@400;500&display=swap">
<style>
  :root {
    --brown: #5e4219;
    --gold: #d3b12c;
    --paper: #ffffff;
    --backdrop: #3a3a3a;
    --rule: #c9a92a;
  }
  * { margin: 0; padding: 0; box-sizing: border-box; }
  html, body { width: 1200px; height: 859px; overflow: hidden; }
  body {
    background: var(--backdrop);
    position: relative;
    font-family: "Montserrat", sans-serif;
  }
  .card {
    position: absolute;
    left: 280px;
    width: 640px;
    height: 366px;
    background: var(--paper);
    overflow: hidden;
    box-shadow: 0 8px 24px rgba(0,0,0,.45);
  }
  .card--front { top: 44px; }
  .card--back { top: 450px; }

  /* Front */
  .brand {
    position: absolute;
    left: 90px;
    top: 130px;
    display: flex;
    align-items: center;
    gap: 18px;
  }
  .brand__dot {
    width: 52px; height: 52px;
    border-radius: 50%;
    background: var(--gold);
  }
  .brand__name {
    font-family: "Cinzel", serif;
    font-weight: 600;
    font-size: 32px;
    color: var(--brown);
    line-height: 1;
  }
  .brand__agent {
    display: flex;
    align-items: center;
    gap: 10px;
    margin-top: 8px;
  }
  .brand__rule { width: 90px; height: 1px; background: var(--brown); }
  .brand__agent-name {
    font-family: "Cinzel", serif;
    font-size: 13px;
    letter-spacing: 3px;
    color: var(--brown);
  }
  .brand__tagline {
    font-family: "Cinzel", serif;
    font-size: 8px;
    letter-spacing: 3px;
    color: var(--brown);
    margin-left: 100px;
    margin-top: 2px;
  }
  .partner-badge {
    position: absolute;
    left: 520px;
    top: 138px;
    width: 48px;
    height: 26px;
    background: var(--brown);
  }

  /* Back */
  .wave { position: absolute; left: 0; top: 0; width: 640px; height: 366px; }
  .mark-area {
    position: absolute;
    left: 460px; top: 36px;
    width: 150px; height: 150px;
    border-radius: 50%;
    background: radial-gradient(circle at 40% 40%, var(--gold), #b8951f);
  }
  .headline {
    position: absolute;
    left: 36px; top: 62px;
    font-family: "Cinzel", serif;
    font-size: 38px;
    letter-spacing: 7px;
    color: var(--brown);
    line-height: 1;
  }
  .headline__tag {
    display: block;
    font-size: 10px;
    letter-spacing: 6px;
    margin: 8px 0 0 62px;
  }
  .edge-dot {
    position: absolute;
    left: -14px; top: 150px;
    width: 30px; height: 30px;
    border-radius: 50%;
    background: var(--brown);
  }
  .contact {
    position: absolute;
    left: 60px; top: 138px;
  }
  .contact__name {
    font-family: "Cinzel", serif;
    font-size: 22px;
    color: var(--gold);
    line-height: 1;
  }
  .contact__role {
    font-family: "Cinzel", serif;
    font-size: 12px;
    color: var(--brown);
    margin-top: 2px;
  }
  .contact__rule {
    width: 190px; height: 1px;
    background: var(--rule);
    margin: 8px 0 10px;
  }
  .contact__list { list-style: none; font-size: 12px; color: var(--brown); }
  .contact__list li { line-height: 19px; }
  .contact__label { color: var(--gold); font-weight: 500; display: inline-block; width: 20px; }
</style>
</head>
<body>

<section class="card card--front" aria-label="Card front">
  <div class="brand">
    <span class="brand__dot"></span>
    <div>
      <div class="brand__name">Cedar Lark Homes</div>
      <div class="brand__agent">
        <span class="brand__rule"></span>
        <span class="brand__agent-name">MAREN QUILL</span>
      </div>
      <div class="brand__tagline">CONNECTED BY TRUST</div>
    </div>
  </div>
  <div class="partner-badge" aria-label="Brindley Vance partner badge"></div>
</section>

<section class="card card--back" aria-label="Card back">
  <svg class="wave" viewBox="0 0 640 366" aria-hidden="true">
    <path d="M0 272 C 140 300, 300 300, 400 250 C 470 215, 520 190, 640 170 L 640 366 L 0 366 Z" fill="var(--gold)"/>
    <path d="M0 286 C 140 314, 300 310, 400 262 C 470 228, 520 204, 640 186 L 640 366 L 0 366 Z" fill="var(--paper)"/>
    <path d="M0 292 C 140 320, 300 316, 400 268 C 470 234, 520 210, 640 192 L 640 366 L 0 366 Z" fill="var(--brown)"/>
  </svg>
  <div class="mark-area" role="img" aria-label="Cedar Lark Homes brand mark"></div>
  <h1 class="headline">MAREN QUILL<span class="headline__tag">CONNECTED BY TRUST</span></h1>
  <span class="edge-dot"></span>
  <div class="contact">
    <div class="contact__name">MAREN QUILL</div>
    <div class="contact__role">ASSOCIATE BROKER</div>
    <div class="contact__rule"></div>
    <ul class="contact__list">
      <li><span class="contact__label">P :</span> 730-418-5093</li>
      <li><span class="contact__label">E :</span> marenquill@cedarlarkhomes.example</li>
      <li><span class="contact__label">W :</span> www.cedarlarkhomes.example</li>
    </ul>
  </div>
</section>

</body>
</html>
```